Site for a workout and Consulting enterprise

I need a professional responsive site for www.valomer.hamburg. The website shoulderstand consist of a Landing and 4 other pages. - On page for the contact informations - on page for the about - on page for consulting services (technical) - on page for Training and workshop services (business and soft skills) I add some files so you can see my idea of the design.
Target Market(s)
IT and Management
Industry/Entity Type
Management Consulting
Coding
Coded - Design and coding required
Number of Pages Required
4 page
Requirements
Must have
- Use Pictures for Background, Sliders and Topics. Just have to placeholders for the design.

```html
<!DOCTYPE html>
<html lang="de">
<head>
<meta charset="utf-8">
<title>Valomer – Individuen, Ideen, Innovationen</title>
<link rel="stylesheet" href="https://fonts.googleapis.com/css2?family=Roboto:wght@300;400&display=swap">
<style>
  :root {
    --photo-dark: #2b241c;
    --photo-mid: #5a4a38;
    --photo-leaf: #8a6a44;
    --photo-green: #3f4a30;
    --panel-blue: rgba(0, 58, 118, 0.9);
    --accent-blue: #3a9be6;
    --text-light: #ffffff;
    --divider-blue: #3a9be6;
  }
  * { margin: 0; padding: 0; box-sizing: border-box; }
  html, body {
    width: 1200px;
    height: 675px;
    overflow: hidden;
    font-family: "Roboto", Arial, sans-serif;
    color: var(--text-light);
  }
  .landing {
    position: relative;
    width: 1200px;
    height: 675px;
    overflow: hidden;
  }
  .hero-photo {
    position: absolute;
    inset: 0;
    background:
      radial-gradient(ellipse at 40% 10%, var(--photo-green) 0%, transparent 55%),
      linear-gradient(170deg, var(--photo-dark) 0%, var(--photo-mid) 45%, var(--photo-leaf) 70%, var(--photo-dark) 100%);
  }
  .brand {
    position: absolute;
    left: 106px;
    top: 250px;
    width: 392px;
  }
  .brand-name {
    font-weight: 300;
    font-size: 104px;
    line-height: 1;
    letter-spacing: 1px;
    white-space: nowrap;
  }
  .brand-tagline {
    margin-top: 14px;
    font-weight: 300;
    font-size: 25.5px;
    line-height: 1.2;
    white-space: nowrap;
  }
  .menu-panel {
    position: absolute;
    left: 601px;
    top: 24px;
    width: 576px;
    height: 627px;
    background: var(--panel-blue);
  }
  .menu-toggle {
    position: absolute;
    left: 34px;
    top: 276px;
    width: 76px;
    height: 76px;
    border-radius: 50%;
    background: var(--accent-blue);
    display: flex;
    align-items: center;
    justify-content: center;
  }
  .panel-footer {
    position: absolute;
    left: 0;
    right: 0;
    bottom: 19px;
    text-align: center;
    padding-left: 0;
    font-size: 16px;
    font-weight: 400;
  }
  .panel-footer nav {
    display: inline-block;
    margin-left: 0;
  }
  .panel-footer a {
    color: var(--text-light);
    text-decoration: none;
  }
  .panel-footer .divider {
    color: var(--divider-blue);
    margin: 0 8px;
  }
</style>
</head>
<body>
  <main class="landing">
    <div class="hero-photo" role="img" aria-label="Hintergrundfoto: herbstliche Bahngleise mit Laub und einer alten Weichenlaterne"></div>

    <header class="brand">
      <div class="brand-name">Valomer</div>
      <p class="brand-tagline">Individuen, Ideen, Innovationen</p>
    </header>

    <aside class="menu-panel">
      <div class="menu-toggle" aria-label="Menü öffnen">
        <svg width="42" height="42" viewBox="0 0 42 42" aria-hidden="true">
          <line x1="21" y1="3" x2="21" y2="39" stroke="#ffffff" stroke-width="2.4"/>
          <line x1="3" y1="21" x2="39" y2="21" stroke="#ffffff" stroke-width="2.4"/>
        </svg>
      </div>
      <footer class="panel-footer">
        <nav>
          <a href="#impressum">Impressum</a><span class="divider">|</span><a href="#kontakt">Kontakt</a>
        </nav>
      </footer>
    </aside>
  </main>
</body>
</html>
```